Website for a Psychologist in Private Practice

I need a cool web design for my website: www.drquorvat.com. I would like it to look professional. Keep all the current content and add: Space for video; radio spots (see Velvet Tide Hour Logo below for those); Quick Inquiry; Brindlepost link; 5 star rating on Zunq; a map; reviews from former patients. I am open to suggestions.

Target Market(s)

Those seeking individual and marital counseling.

Industry/Entity Type

Mental Health

Number of Pages Required

1 page

Font styles to use
Sans Serif
Other font styles liked:
• I'm open but no hard to read script

Requirements
Must have
• All the content on my home page with link for video and radio spots. List services and degrees and expertices (pics not necessary).
Nice to have
• A video of me and radio conversations (logo of Velvet Tide Hour radio attached).
Should not have
• Cartoons, comedy, etc.... I don't need pictures of services (marital, depression, etc...) Just list those.

```html
<!DOCTYPE html>
<html lang="en">
<head>
<meta charset="utf-8">
<title>Dr. Dana L. Quorvat</title>
<link href="https://fonts.googleapis.com/css2?family=Barlow:wght@400;500;600&family=Arimo:ital,wght@0,400;0,700;1,400;1,700&display=swap" rel="stylesheet">
<style>
:root{
  --blue:#2a7fc4;
  --blue-dark:#1f6aa8;
  --navy:#0f3a55;
  --teal:#17676e;
  --teal-dark:#0f4f57;
  --band:rgba(40,52,56,.82);
  --sand:#8c7a66;
  --footer:#232427;
  --white:#fff;
  --light:#dfe7ea;
  --accent:#e8935a;
}
*{margin:0;padding:0;box-sizing:border-box}
html,body{width:744px;height:1200px;overflow:hidden}
body{font-family:"Barlow",sans-serif;color:var(--white);position:relative;
  background:linear-gradient(180deg,#6f9fc4 0%,#b9d2e4 12%,#3bb3c6 30%,#1a8c98 45%,#2c8a8a 58%,#a49383 75%,#c8ae8e 100%)}
.scene{position:absolute;inset:0}
.page{position:absolute;left:82px;top:0;width:581px;height:1200px}
.abs{position:absolute}
.header{left:0;top:0;width:581px;height:58px;background:linear-gradient(180deg,rgba(50,80,110,.55),rgba(40,70,100,.35))}
.brand{left:8px;top:18px;font-size:22px;font-weight:500}
.license{left:358px;top:33px;font-size:9.5px}
.call{left:470px;top:18px}
.call .lbl{font-size:9px;position:absolute;left:20px;top:0;white-space:nowrap}
.call .num{font-size:13.5px;font-weight:500;position:absolute;left:20px;top:12px;white-space:nowrap}
.nav{left:0;top:58px;width:581px;height:28px;background:var(--blue);display:flex;align-items:center;font-size:10px}
.nav a{color:var(--white);text-decoration:none;padding:0 11px;height:28px;line-height:28px;border-right:1px solid rgba(255,255,255,.25)}
.nav a.active{background:var(--blue-dark);color:var(--navy);font-weight:600}
.follow{position:absolute;right:4px;top:5px;display:flex;align-items:center;gap:4px;font-size:8px}
.soc{width:18px;height:18px;border-radius:50%;display:inline-flex;align-items:center;justify-content:center;font-size:6px;font-weight:600}
.hero{left:0;top:86px;width:581px;height:272px;background:linear-gradient(180deg,#c4d8e4 0%,#b6cedd 38%,#2d6f96 52%,#3a7ea0 62%,#9fb8c0 76%,#c2ad8d 100%)}
.hero-text{left:38px;top:100px;color:#24323a}
.hero-text h1{font-size:19px;font-weight:500}
.hero-text p{font-size:14px;line-height:21px;margin-top:2px}
.arrow{width:22px;height:22px;background:#2b2b2b;top:124px}
.cols{left:0;top:358px;width:581px;height:220px;background:rgba(20,80,90,.55)}
.col h2{font-size:13px;font-weight:500;line-height:15px}
.rule{height:3px;background:var(--blue);margin-top:3px;position:relative}
.rule::before{content:"";position:absolute;left:0;top:0;width:60px;height:3px;background:#1b2428}
.body{font-size:8.4px;line-height:13px}
.expert li{list-style:none;font-size:8.4px;line-height:13px;padding-left:11px;position:relative}
.expert li svg{position:absolute;left:0;top:3px}
.quote-box{background:rgba(200,214,216,.82);color:#2b3a40;border-radius:3px;padding:7px 8px;font-size:8.4px;line-height:13px}
.degrees{left:0;top:578px;width:581px;height:50px;background:var(--band)}
.degrees .t{left:66px;top:15px;font-size:14px;font-weight:500}
.degrees .d{font-size:8.4px;line-height:17px}
.lower-title{font-size:14px;font-weight:500}
.video{left:7px;top:676px;width:181px;height:139px;border:2px solid var(--blue);background:linear-gradient(160deg,#3b5d46,#7a8a6b 50%,#4d5f74)}
.form-field{width:172px;height:19px;background:rgba(50,60,66,.6);margin-bottom:3px;font-size:7.5px;padding:5px 6px;color:#d6dadb}
.submit{background:var(--blue);width:68px;height:18px;font-size:9px;font-weight:600;text-align:center;line-height:18px}
.radio{left:404px;top:653px;width:162px;height:162px;background:linear-gradient(135deg,#d12a5c,#d8a0b0 40%,#8d8e92 70%,#c93a64)}
.radio .name{position:absolute;left:6px;top:2px;font-size:14px;font-weight:600;color:#1c1c1c}
.radio .sub{position:absolute;left:4px;top:122px;font-size:9px;line-height:10px;font-weight:600}
.reviews{left:0;top:840px;width:581px;height:182px;background:rgba(70,64,60,.55)}
.reviews h2{position:absolute;left:0;width:581px;text-align:center;top:19px;font-size:14px;font-weight:500}
.reviews .ul{position:absolute;left:196px;top:40px;width:189px;height:1px;background:#d0d0d0}
.reviews .ul::after{content:"";position:absolute;left:70px;top:-1px;width:45px;height:3px;background:var(--blue)}
.avatar{left:7px;top:57px;width:72px;height:72px;border-radius:50%;border:2px solid #fff;background:linear-gradient(180deg,#cfd6da,#3d4a5c)}
.rev-text{left:89px;top:60px;width:475px;font-family:"Arimo",sans-serif;font-style:italic;font-size:7.6px;line-height:14.6px}
.footer{left:0;top:1022px;width:581px;height:152px;background:var(--footer);font-family:"Arimo",sans-serif}
.footer h3{font-size:8.4px;font-weight:400;padding-bottom:5px;border-bottom:1px dashed #666;display:inline-block}
.links a{display:block;color:var(--white);text-decoration:none;font-size:7.6px;line-height:13.6px}
.links a.on{color:var(--accent)}
.contact{font-size:7.6px;line-height:11.6px}
.badge{width:128px;border:2px solid var(--blue)}
.copy{left:0;top:1174px;width:581px;height:26px;background:var(--blue);font-family:"Arimo",sans-serif;font-size:7.6px;text-align:center;line-height:26px}
</style>
</head>
<body>
<div class="scene" role="img" aria-label="Beach scene with sky, clouds, turquoise sea and sand behind the page"></div>
<div class="page">
  <header class="abs header">
    <div class="abs brand">Dr. Dana L. Quorvat</div>
    <div class="abs license">California # PSY20481</div>
    <div class="abs call">
      <svg width="16" height="16" viewBox="0 0 16 16" style="position:absolute;left:0;top:6px"><circle cx="8" cy="8" r="7" fill="none" stroke="#fff" stroke-width="1"/><path d="M5.5 4.5l2 1.5-1 1.5c.5 1 1.3 1.8 2.3 2.3l1.5-1 1.5 2-1 1.2C7.5 11.5 4.5 8.5 4.5 5.5z" fill="#fff"/></svg>
      <span class="lbl">Call Us Today</span>
      <span class="num">555-210-4830</span>
    </div>
  </header>
  <nav class="abs nav">
    <a class="active">Home</a><a>About Me</a><a>Sessions</a><a>Resources</a><a>BIO</a><a>Customer Reviews</a><a style="border:0">Contact Us</a>
    <div class="follow">Follow Us On
      <span class="soc" style="background:#3b5998">Brindlepost</span>
      <span class="soc" style="background:#2aa9e0">Chirpline</span>
    </div>
  </nav>
  <section class="abs hero" role="img" aria-label="Woman with arms outstretched on a beach by the sea">
    <div class="abs hero-text">
      <h1>Dr. Dana L. Quorvat</h1>
      <p>The Best way to Conquer a<br>problem is to FACE it</p>
    </div>
    <div class="abs arrow" style="left:1px"><svg width="22" height="22"><path d="M13 6l-5 5 5 5" stroke="#fff" stroke-width="2" fill="none"/></svg></div>
    <div class="abs arrow" style="right:7px"><svg width="22" height="22"><path d="M9 6l5 5-5 5" stroke="#fff" stroke-width="2" fill="none"/></svg></div>
  </section>

  <section class="abs cols">
    <div class="abs col" style="left:7px;top:22px;width:174px">
      <h2>About<br>Dr. Dana L. Quorvat</h2>
      <div class="rule"></div>
      <p class="body" style="margin-top:12px">While I acknowledge the importance of my education, I also appreciate the role my experiences have played in allowing me to relate so well to others. Allow me to share those I feel are most relevant with you.<br>I survived an abusive childhood that my mother &amp; sister unfortunately did not. &amp; it was my grief &amp; desire to become stronger than my past that led me to counseling.....</p>
      <p class="body" style="text-decoration:underline;margin-top:1px">Read More</p>
    </div>
    <div class="abs" style="left:184px;top:22px;width:1px;height:180px;background:rgba(255,255,255,.3)"></div>
    <div class="abs col" style="left:206px;top:22px;width:172px">
      <h2>My<br>Expertise</h2>
      <div class="rule"></div>
      <div class="abs" role="img" aria-label="Portrait of the psychologist" style="left:-4px;top:42px;width:64px;height:64px;border-radius:50%;border:2px solid #fff;background:linear-gradient(160deg,#d9c39a,#4f6a82)"></div>
      <div class="abs" style="left:66px;top:55px;font-size:13px;line-height:17px;font-weight:500">Dr. Dana L.<br>Quorvat</div>
      <ul class="abs expert" style="left:4px;top:110px;width:180px">
        <li><svg width="8" height="8"><path d="M1 4l2 2 4-5" stroke="#fff" stroke-width="1.5" fill="none"/></svg>Dating, Marriage,</li>
        <li><svg width="8" height="8"><path d="M1 4l2 2 4-5" stroke="#fff" stroke-width="1.5" fill="none"/></svg>Parenting &amp; Professional Relationships</li>
        <li><svg width="8" height="8"><path d="M1 4l2 2 4-5" stroke="#fff" stroke-width="1.5" fill="none"/></svg>Depression &amp; Anxiety Issues</li>
        <li><svg width="8" height="8"><path d="M1 4l2 2 4-5" stroke="#fff" stroke-width="1.5" fill="none"/></svg>Personality Disorders</li>
        <li><svg width="8" height="8"><path d="M1 4l2 2 4-5" stroke="#fff" stroke-width="1.5" fill="none"/></svg>Life Management</li>
      </ul>
    </div>
    <div class="abs col" style="left:400px;top:22px;width:174px">
      <h2>Radio<br>Conversations</h2>
      <div class="rule"></div>
      <div class="quote-box" style="margin-top:12px;height:104px">
        <span style="font-size:14px;color:#8a9aa0;font-weight:600">&ldquo;</span> Lorem ipsum dolor sit ae onsectetuer adipiscing elit, sed diam nonummy nibh euis tincidunt ut laoreetlore gna aliquam erat olutpat. Ut wisi enim adinim veniam, quis strud xerci tation ullamrper suscipit lobortis sl ut al lorem.
        <div style="text-align:right;font-size:7.6px;font-family:serif;margin-top:2px">Jane Marlow</div>
      </div>
      <p class="body" style="text-decoration:underline;margin-top:6px">View All</p>
    </div>
  </section>

  <section class="abs degrees">
    <div class="abs t">My Degrees</div>
    <svg class="abs" style="left:146px;top:8px" width="12" height="36"><path d="M2 1c6 2 5 12 8 17-3 5-2 15-8 17" stroke="#ccc" fill="none"/></svg>
    <div class="abs d" style="left:171px;top:8px">Doctoral Degree in Clinical Psychology<br>Masters Degree in Counseling Psychology</div>
    <div class="abs d" style="left:360px;top:8px">Doctoral Internship, Coastal University Medical Center<br>Masters Internship, Westbrook Clinic</div>
  </section>

  <div class="abs" style="left:6px;top:650px;width:183px">
    <div class="lower-title">View Video</div><div class="rule"></div>
  </div>
  <div class="abs video" role="img" aria-label="Video still of the psychologist">
    <svg class="abs" style="left:79px;top:59px" width="20" height="20"><circle cx="10" cy="10" r="8.5" stroke="#fff" stroke-width="1.5" fill="none"/><path d="M8 6l5 4-5 4z" fill="#fff"/></svg>
  </div>

  <div class="abs" style="left:211px;top:650px;width:175px">
    <div class="lower-title">Quick Inquiry</div><div class="rule"></div>
    <p style="font-size:7.2px;margin:11px 0 5px">Lorem ipsum dolor sit amet, consectetuer</p>
    <div class="form-field">Name</div>
    <div class="form-field">Email</div>
    <div class="form-field">Phone</div>
    <div class="form-field" style="height:32px;padding-top:3px">Message</div>
    <div class="submit" style="margin-top:2px">SUBMIT</div>
  </div>

  <div class="abs radio" role="img" aria-label="Velvet Tide Hour radio show poster with hosts and the psychologist">
    <div class="name">Velvet Tide Hour</div>
    <div style="position:absolute;left:22px;top:17px;font-size:9px;color:#fff;font-weight:500">With Mara and Lina</div>
    <div class="sub">SUNDAYS<br>4PM PST/7PM EST<br>TIDEWAVERADIO.COM</div>
  </div>

  <section class="abs reviews">
    <h2>Reviews From Former Patients</h2>
    <div class="ul"></div>
    <div class="abs avatar" role="img" aria-label="Portrait of a former patient"></div>
    <div class="abs rev-text"><span style="font-size:18px;color:#b8b8b8;font-style:normal;vertical-align:-6px">&ldquo;</span> Lorem ipsum dolor sit amet, consectetuer adipiscing elit, sed diam nonummy nibh euismod tincidunt ut laoreet dolore magna aliquam erat volutpat. Ut wisi enim ad minim veniam, quis nostrud exerci tation ullamcorper suscipit lobortis nisl ut aliquip commodo consequat. Duis autem vel eum iriure dolor in hendrerit in vulputate velit esse molestie consequat, vel illum dolore eu feugiat nulla facilisis at vero eros et accumsan et iusto odio dignissimaugue duis dolore te feugait nulla facilisi.
      <div style="font-weight:700;margin-top:5px">.... Lorem Ispum, Manger</div>
    </div>
    <div class="abs" style="right:6px;top:143px;font-family:Arimo,sans-serif;font-size:7.6px;text-decoration:underline">Read more testimonials <span style="text-decoration:none">&raquo;</span></div>
  </section>

  <footer class="abs footer">
    <div class="abs links" style="left:8px;top:20px">
      <h3 style="width:74px">Quick Links</h3>
      <div style="margin-top:6px">
        <a class="on">Home</a><a>About Me</a><a>Sessions</a><a>Resources</a><a>BIO</a><a>Customer Reviews</a><a>Contact Me</a>
      </div>
    </div>
    <div class="abs" style="left:130px;top:20px">
      <h3>A Portion of All Revenue Is Donated To</h3>
      <div class="badge" style="margin-top:6px;height:49px;background:#fff"></div>
      <div class="badge" style="margin-top:4px;height:47px;background:#8ea43e"></div>
    </div>
    <div class="abs contact" style="left:341px;top:20px">
      <h3 style="width:100px">Contact Details</h3>
      <div style="display:flex;margin-top:9px"><span style="width:18px">A:</span><span>418 Harbor Lane, Suite 120<br>Seaview, CA 90000</span></div>
      <div style="display:flex;margin-top:10px"><span style="width:18px">P:</span><span>555-210-4830</span></div>
      <div style="display:flex;margin-top:9px"><span style="width:20px">TF:</span><span>555-210-4830</span></div>
      <div style="display:flex;margin-top:9px"><span style="width:18px">E:</span><span>dq@drquorvat.com</span></div>
    </div>
    <div class="abs" style="left:513px;top:37px;width:50px;height:48px;border-radius:6px;background:#c4242b;display:flex;align-items:center;justify-content:center;font-size:11px;font-weight:700">Zunq</div>
    <div class="abs" style="left:510px;top:98px;width:58px;height:18px;background:#3e5c99;border:1px solid #6f87b8;display:flex;align-items:center;justify-content:center;gap:4px;font-size:7px">
      <span style="width:8px;height:8px;background:#fff;display:inline-block"></span>Brindlepost
    </div>
  </footer>
  <div class="abs copy">Copyright &copy; 2016 Dr. Dana L. Quorvat &nbsp;All rights reserved</div>
</div>
</body>
</html>
```